Harrowgate Estates Business Card for Apartment Buildings

Create business cards for resident managers who run apartment buildings. The audience is the public who are searching for apartment rentals, and current residents who live at the apartment building. Key design element will be incorporating the company logo, however, the logo cannot dominate. The building name and manager name are more important than the logo. Current business card design leaves little room for copy, so we may need to reduce the size on the current card to allow for more space for copy.

Target Market(s)

Adults 18-65 years of age, who are looking for an apartment rental, plus current residents who live at our apartment buildings.

Industry/Entity Type

Property Management

Contact Information for Business Card

A major design element will be use of the company logo. Important property and manager contact information must be part of the design. The size of the logo will need to be reduced to make room for building and manager contact copy.

Font styles to use
Sans Serif

Colors
3176b5
000000
959595
ffffff

Requirements
Must have
• 1) Incorporate the company logo.
• 2) Use the company colors (dark blue, black/grey, over white).
• 3) FEATURE THE BUILDING NAME
• 4) FEATURE THE MANAGER NAME
• 5) The company name is less important than BUILDING and MANAGER
• 6) Manager contact information
• **SEE ATTACHED CREATIVE BRIEF**
Nice to have
• 1) Back of card logo watermark
• 2) Ability to write notes on back of carfd
Should not have
• Avoid letting the company logo dominate the card, the building name and manager are more important than the company logo.

```html
<!DOCTYPE html>
<html lang="en">
<head>
<meta charset="utf-8">
<title>Harrowgate Estates Business Card</title>
<link href="https://fonts.googleapis.com/css2?family=Lato:wght@400;700;900&display=swap" rel="stylesheet">
<style>
  :root {
    --stage: #f7861e;
    --brand-blue: #1b6aa8;
    --ink: #0d1b33;
    --grey: #959595;
    --paper: #ffffff;
    --paper-tint: #f3f3f3;
  }
  * { margin: 0; padding: 0; box-sizing: border-box; }
  html, body { width: 1200px; height: 900px; overflow: hidden; }
  body {
    background: var(--stage);
    font-family: "Lato", sans-serif;
    position: relative;
  }
  .card {
    position: absolute;
    top: 271px;
    width: 540px;
    height: 307px;
    overflow: hidden;
  }
  .card--front { left: 33px; background: var(--paper); }
  .card--back { left: 623px; background: var(--brand-blue); }
  .card__texture {
    position: absolute; inset: 0;
  }
  .card--front .card__texture { background: var(--paper-tint); }
  .card--back .card__texture { background: #1d6dab; }

  .brand {
    position: absolute;
    display: flex;
    align-items: center;
    gap: 10px;
    font-weight: 900;
    white-space: nowrap;
  }
  .brand__square { width: 26px; height: 26px; flex: none; }
  .card--front .brand { left: 150px; top: 42px; color: var(--brand-blue); font-size: 30px; }
  .card--front .brand__square { background: var(--brand-blue); }
  .card--back .brand { left: 0; right: 0; justify-content: center; top: 128px; color: var(--paper); font-size: 36px; }
  .card--back .brand__square { background: var(--paper); width: 30px; height: 30px; }

  .manager {
    position: absolute;
    left: 39px;
    top: 138px;
  }
  .manager__name { font-size: 19px; font-weight: 900; color: var(--ink); }
  .manager__title { font-size: 13px; color: var(--ink); margin-top: 1px; }

  .divider {
    position: absolute;
    left: 236px; top: 118px;
    width: 1px; height: 94px;
    background: var(--grey);
  }

  .contact {
    position: absolute;
    left: 264px; top: 121px;
    list-style: none;
    color: var(--ink);
    font-size: 14.5px;
    line-height: 18.6px;
  }
  .contact li { display: flex; align-items: center; }
  .contact__icon { width: 14px; height: 14px; margin-right: 11px; flex: none; }
  .contact__strong { font-weight: 700; }

  .website {
    position: absolute;
    left: 0; right: 0; top: 255px;
    text-align: center;
    color: var(--paper);
    font-size: 19px;
    letter-spacing: 3.4px;
  }
</style>
</head>
<body>

<section class="card card--front" aria-label="Business card front">
  <div class="card__texture" role="img" aria-label="Subtle light grey square pattern background"></div>
  <div class="brand"><span class="brand__square"></span>Harrowgate Estates</div>

  <div class="manager">
    <p class="manager__name">Marisol Ortega</p>
    <p class="manager__title">Resident Manager</p>
  </div>

  <div class="divider"></div>

  <ul class="contact">
    <li class="contact__strong">
      <svg class="contact__icon" viewBox="0 0 14 14"><path d="M3 1.5l2 .2 1 3-1.4 1a7 7 0 0 0 3.7 3.7l1-1.4 3 1 .2 2c-.3 1-1.3 1.5-2.3 1.3A10 10 0 0 1 1.7 3.8C1.5 2.8 2 1.8 3 1.5z" fill="var(--ink)"/></svg>
      555-214-3870</li>
    <li class="contact__strong">
      <svg class="contact__icon" viewBox="0 0 14 14"><rect x="2" y="4" width="10" height="7" rx="1.5" fill="none" stroke="var(--ink)" stroke-width="1.4"/><rect x="4" y="1.5" width="6" height="3" fill="none" stroke="var(--ink)" stroke-width="1.2"/><rect x="5" y="7" width="4" height="1.2" fill="var(--ink)"/></svg>
      555-214-3871</li>
    <li class="contact__strong"><span class="contact__icon"></span>555-482-9105</li>
    <li class="contact__strong">
      <svg class="contact__icon" viewBox="0 0 14 14"><rect x="1.5" y="3" width="11" height="8" fill="none" stroke="var(--ink)" stroke-width="1.2"/><path d="M1.5 3L7 8l5.5-5" fill="none" stroke="var(--ink)" stroke-width="1.2"/></svg>
      marisol@harrowgate.com</li>
    <li>
      <svg class="contact__icon" viewBox="0 0 14 14"><path d="M7 13S2.5 8 2.5 5.2a4.5 4.5 0 0 1 9 0C11.5 8 7 13 7 13z" fill="var(--ink)"/><circle cx="7" cy="5.2" r="1.7" fill="var(--paper)"/></svg>
      Cedar Court Apartments</li>
    <li><span class="contact__icon"></span>1482 Larkspur Avenue</li>
    <li><span class="contact__icon"></span>Fairview, CA 90000</li>
  </ul>
</section>

<section class="card card--back" aria-label="Business card back">
  <div class="card__texture" role="img" aria-label="Subtle blue square pattern background"></div>
  <div class="brand"><span class="brand__square"></span>Harrowgate Estates</div>
  <p class="website">WWW.HARROWGATE.COM</p>
</section>

</body>
</html>
```